Website front page and logo re-designed (using logo provided)

We are looking for the home page of our new website. It is a website offering a space for clients to ask professionals questions. The website should be similar in design to www.brimtolo.com however it is clear it should be a different look. It should be modern, simple to use, a clear navigation bar at the top and bottom.

Logo should be similar to the one attached, but more professional and modern. Logo should be clearly incorporated into website. Design should focus on our website colours as in the logo.

Logo Text

Kelvora - Clarity at every turn!

Number of Pages Required

1 page

Font styles to use
Sans Serif

```html
<!DOCTYPE html>
<html lang="en">
<head>
<meta charset="utf-8">
<title>Kelvora - Clarity at every turn!</title>
<link href="https://fonts.googleapis.com/css2?family=Roboto:ital,wght@0,400;0,500;0,700;1,400&display=swap" rel="stylesheet">
<style>
:root{
  --green:#3a9a1a;--red:#d93a0c;--dark:#222;--darker:#191919;--ink:#444;--muted:#666;
  --band:#efefef;--line:#ddd;--white:#fff;
}
*{box-sizing:border-box;margin:0;padding:0}
html,body{width:1200px;height:1200px;overflow:hidden;background:#fff;font-family:'Roboto',sans-serif;color:var(--ink)}
.stage{width:1500px;height:1500px;transform:scale(.8);transform-origin:0 0;position:relative}
.a{position:absolute}
.brand{font-weight:700;color:var(--green);font-size:22px;line-height:1}
.tag{font-size:7px;color:#333}
.nav a{position:absolute;top:28px;font-size:7px;color:#555;text-decoration:none}
.phone{left:928px;top:6px;font-size:7px;color:var(--red)}
.help{left:992px;top:4px;width:29px;height:12px;background:#111;color:#fff;font-size:7px;text-align:center;line-height:12px}
.search{left:907px;top:26px;width:114px;height:15px;border:1px solid #ccc}
.rule{left:297px;top:48px;width:906px;height:2px;background:#e6e6e6}
.photo{background:linear-gradient(90deg,#fff 0%,#e9edf1 35%,#d6dee6 60%,#fff 100%)}
h1.q{left:479px;top:72px;font-size:19px;font-weight:700;color:var(--red)}
.sub{left:479px;top:98px;font-size:19px;color:#333;font-weight:500}
.ask{left:478px;top:141px;width:380px;height:202px;background:#2a2a2a}
.tabs{left:484px;top:148px;font-size:6.5px;color:#fff;display:flex;gap:8px;align-items:center}
.tabs .on{background:#fff;color:#222;padding:2px 4px;border-radius:2px}
.box{left:484px;top:167px;width:366px;height:93px;background:#fff;border-radius:2px}
.lbl{font-size:7.5px;color:#fff}
.sel{left:726px;top:275px;width:124px;height:14px;background:#fff;font-size:6px;color:#777;padding:3px 5px}
.btn{background:var(--red);color:#fff;font-weight:700;font-size:9px;text-align:center;border-radius:2px}
.h2{font-size:14px;font-weight:500;color:#444;text-align:center}
.feat{width:160px;text-align:center}
.feat svg{display:block;margin:0 auto}
.feat b{display:block;font-weight:400;font-size:9px;color:#333;margin-top:8px;letter-spacing:.3px}
.feat p{font-size:6px;color:#777;margin-top:6px;line-height:1.55}
.gs{left:875px;top:538px;width:121px;height:87px;border:1px solid var(--green)}
.gs .hd{height:27px;background:var(--green);color:#fff;font-size:14px;text-align:center;line-height:27px}
.band{left:297px;top:651px;width:906px;height:217px;background:var(--band)}
table{border-collapse:collapse;width:543px;font-size:6.5px;color:#555;border:1px solid var(--green);background:#fff}
th{background:var(--green);color:#fff;font-weight:500;font-size:9px;height:22px;text-align:left;padding-left:9px}
td{height:18.7px;border-top:1px solid #eee;padding-left:9px}
.st{color:var(--red);letter-spacing:3px;font-size:8px}.st i{color:#555;font-style:normal}
.exp{width:130px;text-align:center}
.face{width:72px;height:72px;border-radius:50%;margin:0 auto;background:radial-gradient(circle at 50% 40%,#c89a80,#4a3a34 70%)}
.exp .nm{font-size:8.5px;color:#444;margin-top:4px}
.exp p{font-size:6.5px;color:#555;line-height:1.4;margin-top:3px}
.press{left:297px;top:1090px;width:906px;height:51px;background:var(--red)}
.pb{position:absolute;top:17px;height:17px;background:rgba(255,255,255,.85);border-radius:3px}
.testi{left:297px;top:1141px;width:906px;height:186px;background:linear-gradient(90deg,#6b6b6b,#5a5a5a 60%,#707070)}
.quote{left:505px;top:1222px;width:490px;font-size:8.5px;font-style:italic;color:#eee;text-align:center;line-height:1.7}
.gbar{left:297px;top:1327px;width:906px;height:20px;background:var(--green);color:#fff;font-size:6.5px}
.foot{left:297px;top:1347px;width:906px;height:121px;background:var(--dark)}
.fh{font-size:8.5px;color:#fff}
.fl{font-size:6.5px;color:#aaa;line-height:14.4px}
.bottom{left:297px;top:1468px;width:906px;height:26px;background:var(--darker);font-size:6px;color:#aaa}
</style>
</head>
<body>
<div class="stage">
  <header>
    <div class="a" style="left:479px;top:10px"><div class="brand">Kelvora</div><div class="tag" style="margin:3px 0 0 7px">Clarity at every turn!</div></div>
    <nav class="nav">
      <svg class="a" style="left:674px;top:27px" width="10" height="9" viewBox="0 0 10 9"><path d="M5 0 10 5H8.5V9H6V6H4V9H1.5V5H0Z" fill="#d93a0c"/></svg>
      <a style="left:700px">How It Works</a><a style="left:753px">About Us</a><a style="left:794px">Browse</a><a style="left:830px">Login</a><a style="left:860px">Sign Up</a>
    </nav>
    <div class="a phone">(415) 0207-5581 or</div>
    <div class="a help">Help</div>
    <div class="a search"><svg class="a" style="right:3px;top:2px" width="10" height="10" viewBox="0 0 10 10"><circle cx="4" cy="4" r="3" fill="none" stroke="#888"/><path d="M6.3 6.3 9.5 9.5" stroke="#888"/></svg></div>
    <div class="a rule"></div>
  </header>

  <section>
    <div class="a photo" role="img" aria-label="Smiling young professional in glasses and a light shirt" style="left:740px;top:50px;width:290px;height:316px"></div>
    <div class="a" style="left:465px;top:50px;width:2px;height:316px;background:#f0f0f0"></div>
    <div class="a photo" role="img" aria-label="Blurred office background" style="left:478px;top:342px;width:380px;height:24px;background:linear-gradient(90deg,#6c6c6c,#9aa0a6)"></div>
    <h1 class="a q">Have a Question?</h1>
    <div class="a sub">"Ask for expert Answers you can count on! "</div>
    <div class="a ask"></div>
    <div class="a tabs"><span class="on">Lawyers ▾</span><span>Mechanics</span><span>Doctors &amp; Nurses</span><span>Vets</span><span>Electricians &amp; Plumbers</span><span>Computer &amp; Education</span><span>MoreCategories</span></div>
    <div class="a box"></div>
    <div class="a lbl" style="left:596px;top:278px">Would you like to select a specialist:</div>
    <div class="a sel">Optional<span style="float:right;color:#222">▾</span></div>
    <div class="a lbl" style="left:656px;top:313px;font-size:7px">32 Experts are Online Now</div>
    <div class="a btn" style="left:752px;top:305px;width:98px;height:22px;line-height:22px">Get an Answer</div>
  </section>

  <section>
    <div class="a h2" style="left:600px;top:389px;width:300px">Why ask a question ?</div>
    <div class="a feat" style="left:484px;top:435px">
      <svg width="32" height="30" viewBox="0 0 32 30"><path d="M16 2a6 6 0 0 0-6 6c0 5 6 11 6 11s6-6 6-11a6 6 0 0 0-6-6z" fill="none" stroke="#3a9a1a" stroke-width="3"/><path d="M2 29 8 17h5M19 17h5l6 12z" fill="#3a9a1a"/></svg>
      <b>CONVENIENCE</b><p>ENJOY A FAST, EASY WAY TO ASK EXPERTS ANY-WHERE YOU'RE ONLINE.</p></div>
    <div class="a feat" style="left:669px;top:433px">
      <svg width="32" height="32" viewBox="0 0 32 32"><path d="M12 3v16l-3-3c-2-1-3 1-2 2l6 8c1 2 3 3 5 3h2c4 0 6-3 6-6v-7c0-2-3-2-3 0v-2c0-2-3-2-3 0v-1c0-2-3-2-3 0V3c0-2-3-2-3 0z" fill="none" stroke="#3a9a1a" stroke-width="1.6"/></svg>
      <b>ONE ON ONE</b><p>ENJOY A FAST, EASY WAY TO ASK EXPERTS ANY-WHERE YOU'RE ONLINE.</p></div>
    <div class="a feat" style="left:853px;top:434px">
      <svg width="30" height="30" viewBox="0 0 30 30"><circle cx="15" cy="15" r="12" fill="none" stroke="#3a9a1a" stroke-width="3"/><circle cx="15" cy="15" r="7" fill="none" stroke="#3a9a1a" stroke-width="2"/><path d="M15 11v4h3" stroke="#3a9a1a" stroke-width="1.6" fill="none"/></svg>
      <b>24/7 AVAILABILITY</b><p>ENJOY A FAST, EASY WAY TO ASK EXPERTS ANY-WHERE YOU'RE ONLINE.</p></div>
    <div class="a feat" style="left:484px;top:538px">
      <svg width="34" height="34" viewBox="0 0 34 34"><circle cx="15" cy="19" r="13" fill="none" stroke="#3a9a1a" stroke-width="3"/><circle cx="15" cy="19" r="7" fill="none" stroke="#3a9a1a" stroke-width="2.5"/><path d="M15 19 30 4" stroke="#3a9a1a" stroke-width="2.5"/><path d="M27 2h5v5z" fill="#3a9a1a"/></svg>
      <b>BROAD EXPERTISE</b><p>ENJOY A FAST, EASY WAY TO ASK EXPERTS ANY-WHERE YOU'RE ONLINE.</p></div>
    <div class="a feat" style="left:669px;top:538px">
      <svg width="36" height="36" viewBox="0 0 36 36"><circle cx="18" cy="18" r="16" fill="none" stroke="#3a9a1a" stroke-width="3"/><circle cx="12" cy="14" r="2.2" fill="#3a9a1a"/><circle cx="24" cy="14" r="2.2" fill="#3a9a1a"/><path d="M10 21c4 6 12 6 16 0" fill="none" stroke="#3a9a1a" stroke-width="2.5"/></svg>
      <b>100% SATISFACTION</b><p>ENJOY A FAST, EASY WAY TO ASK EXPERTS ANY-WHERE YOU'RE ONLINE.</p></div>
    <div class="a gs"><div class="hd">Get Started</div><div class="btn" style="margin:19px auto 0;width:99px;height:21px;line-height:21px">Get an Answer</div></div>
  </section>

  <section class="a band">
    <div class="h2" style="margin-top:21px;line-height:17px">Join the 5 million people<br>who found a smarter way to get Expert help</div>
    <table style="position:absolute;left:181px;top:78px">
      <tr><th>Recently answered questions</th><th style="width:90px;text-align:center;padding:0;font-weight:400;font-size:8px">Rating</th><th style="width:90px;text-align:center;padding:0;font-weight:400;font-size:8px">Date</th></tr>
      <tr><td>Lorem ipsum dolor sit amet, consectetur adipiscing elit. Quisque</td><td class="st" style="text-align:center">★★★★<i>★</i></td><td style="text-align:center">6 hours ago</td></tr>
      <tr><td>luctus nisi non augue consectetur, id elementum</td><td class="st" style="text-align:center">★★★★★</td><td style="text-align:center">7 hours ago</td></tr>
      <tr><td>sodales eros urna, vitae elementum enim malesuada ut.</td><td class="st" style="text-align:center">★★★★<i>★</i></td><td style="text-align:center">8 hours ago</td></tr>
      <tr><td>Proin placerat commodo mattis. Pellentesque sit amet</td><td class="st" style="text-align:center">★★★★★</td><td style="text-align:center">9 hours ago</td></tr>
      <tr><td>Lorem ipsum dolor sit amet, consectetur adipiscing elit. Quisque</td><td class="st" style="text-align:center">★★★★<i>★</i></td><td style="text-align:center">10 hours ago</td></tr>
    </table>
  </section>

  <section>
    <div class="a h2" style="left:600px;top:893px;width:300px">Our Experts</div>
    <svg class="a" style="left:477px;top:980px" width="12" height="38" viewBox="0 0 12 38"><path d="M11 1 1 19l10 18" fill="none" stroke="#999" stroke-width="1.5"/></svg>
    <svg class="a" style="left:1010px;top:980px" width="12" height="38" viewBox="0 0 12 38"><path d="M1 1l10 18L1 37" fill="none" stroke="#999" stroke-width="1.5"/></svg>
    <div class="a exp" style="left:476px;top:932px"><div class="face" role="img" aria-label="Portrait of expert Orin Halvey"></div><div class="st" style="margin-top:6px">★★★★<i>★</i></div><div class="nm">Orin Halvey, us</div><p>consectetur adipiscing elit. Quisque luctus nisi non augue consectetur, id elementum nibh</p></div>
    <div class="a exp" style="left:615px;top:932px"><div class="face" role="img" aria-label="Portrait of expert Mr. Daskell" style="background:radial-gradient(circle at 50% 40%,#b48a70,#3e4a55 70%)"></div><div class="st" style="margin-top:6px">★★★★<i>★</i></div><div class="nm">Mr. Daskell, us</div><p>consectetur adipiscing elit. Quisque luctus nisi non augue consectetur, id elementum nibh</p></div>
    <div class="a exp" style="left:754px;top:932px"><div class="face" role="img" aria-label="Portrait of expert Tobias Wrenfield" style="background:radial-gradient(circle at 50% 40%,#c99a7a,#1f5fa8 65%)"></div><div class="st" style="margin-top:6px">★★★★<i>★</i></div><div class="nm">Tobias Wrenfield, us</div><p>consectetur adipiscing elit. Quisque luctus nisi non augue consectetur, id elementum nibh</p></div>
    <div class="a exp" style="left:894px;top:932px"><div class="face" role="img" aria-label="Portrait of expert Mirela Sontag" style="background:radial-gradient(circle at 50% 40%,#e3b49a,#5a2a22 70%)"></div><div class="st" style="margin-top:6px">★★★★<i>★</i></div><div class="nm">Mirela Sontag us</div><p>consectetur adipiscing elit. Quisque luctus nisi non augue consectetur, id elementum nibh</p></div>
  </section>

  <section class="a press" aria-label="As seen in">
    <div class="pb" style="left:228px;width:34px"></div>
    <div class="pb" style="left:318px;width:38px"></div>
    <div class="pb" style="left:408px;width:96px"></div>
    <div class="pb" style="left:556px;width:26px;top:15px;height:22px"></div>
    <div class="pb" style="left:647px;width:28px"></div>
  </section>

  <section>
    <div class="a testi" role="img" aria-label="Muted photo of a doctor with a stethoscope"></div>
    <div class="a" style="left:505px;top:1192px;font-size:34px;color:#bbb;font-weight:700;line-height:1">“</div>
    <svg class="a" style="left:480px;top:1214px" width="12" height="38" viewBox="0 0 12 38"><path d="M11 1 1 19l10 18" fill="none" stroke="#fff" stroke-width="2"/></svg>
    <svg class="a" style="left:1008px;top:1214px" width="12" height="38" viewBox="0 0 12 38"><path d="M1 1l10 18L1 37" fill="none" stroke="#fff" stroke-width="2"/></svg>
    <div class="a quote">Morbi id lorem urna. Fusce nec ante eros. Aenean pharetra risus id ex dapibus commodo. Mauris imperdiet erat quis mattis ornare. Sed volutpat lorem eu risus rutrum ultricies. Ut ullamcorper urna ac interdum accumsan.</div>
    <div class="a" style="left:900px;top:1259px;width:108px;text-align:right;font-size:9px;color:#fff;font-weight:500">Harlan Quist.</div>
  </section>

  <footer>
    <div class="a gbar">
      <span class="a" style="left:203px;top:6px;width:7px;height:7px;border-radius:50%;background:#fff"></span>
      <span class="a" style="left:216px;top:5px">@kelvorahq: New guides on asking sharper questions today..</span>
      <span class="a" style="left:613px;top:4px;font-size:8.5px">Contact Us</span>
      <svg class="a" style="left:548px;top:20px" width="8" height="4"><path d="M0 0h8L4 4z" fill="#3a9a1a"/></svg>
    </div>
    <div class="a foot"></div>
    <div class="a" style="left:478px;top:1357px;width:116px;height:48px;background:#fff;padding:8px 0 0 4px"><div class="brand" style="font-size:21px">Kelvora</div><div class="tag" style="margin:2px 0 0 7px">Clarity at every turn!</div></div>
    <div class="a" style="left:478px;top:1411px;width:116px;height:47px;background:#fff"><div style="margin:10px auto 0;width:64px;height:28px;border-radius:50%;background:#1f4f9a" role="img" aria-label="Satisfaction guaranteed badge"></div></div>
    <div class="a" style="left:627px;top:1362px"><div class="fh">Categories</div><div class="fl" style="margin:2px 0 0 5px">About Us<br>Help FAQs<br>Our Promise<br>Login<br>Register</div></div>
    <div class="a" style="left:769px;top:1362px"><div class="fh">Useful Links</div><div class="fl" style="margin:2px 0 0 5px">Careers<br>Become an Expert<br>Become an Affiliate<br>Refer an Expert</div></div>
    <div class="a" style="left:911px;top:1366px;width:110px;font-size:6px;color:#aaa;line-height:1.4">This is our quick note about the team. Proin gravida nibh vel velit auctor aliquet.</div>
    <div class="a" style="left:911px;top:1400px;font-size:6px;color:#aaa;line-height:12.5px">
      <div><span style="color:#fff;margin-right:8px">⚲</span>48 Harrow Lane, Oakridge, USA</div>
      <div><span style="color:#fff;margin-right:8px">✆</span>+ 415 208 3341 / + 415 208 3342</div>
      <div><span style="color:#fff;margin-right:8px">✉</span><span style="color:var(--green)">contact@brimtolo.com</span></div>
    </div>
    <div class="a bottom">
      <span class="a" style="left:181px;top:10px">Copyright 2016 Kelvora. All Rights Reserved.</span>
      <span class="a" style="left:627px;top:9px;width:7px;height:7px;border-radius:50%;background:#ddd"></span>
      <span class="a" style="left:644px;top:9px;width:7px;height:7px;border-radius:50%;background:#ddd"></span>
      <span class="a" style="left:661px;top:9px;width:7px;height:7px;border-radius:50%;background:#ddd"></span>
      <span class="a" style="left:678px;top:9px;width:7px;height:7px;border-radius:50%;background:#ddd"></span>
    </div>
  </footer>
</div>
</body>
</html>
```